Marrowin Brook Salon jojoba oil

Hello there!
I am looking to have a label created for a jojoba oil product I am launching. I have attached the logo of my company below. The label should have the following information on it as well:
Ingredients: pure jojoba oil
Size of the bottle: 118ml
And there might be more but I am working on this and will keep you posted.

```html
<!DOCTYPE html>
<html lang="en">
<head>
<meta charset="utf-8">
<title>Marrowin Brook Salon – Pure Jojoba Oil Label</title>
<link href="https://fonts.googleapis.com/css2?family=Playfair+Display:wght@500&family=Cinzel:wght@400&family=Raleway:wght@300&family=Montserrat:wght@500;600&display=swap" rel="stylesheet">
<style>
  :root {
    --backdrop: #525252;
    --label: #ffffff;
    --ink: #111111;
    --gold-light: #d9ba75;
    --gold-mid: #c9963f;
    --gold-pale: #d6c088;
    --gold-text: #c8973f;
    --botanical: #fbefd2;
  }
  * { margin: 0; padding: 0; box-sizing: border-box; }
  html, body { width: 1200px; height: 1200px; overflow: hidden; }
  body { background: var(--backdrop); position: relative; }

  .label {
    position: absolute; left: 390px; top: 180px;
    width: 420px; height: 840px;
    background: var(--label);
    box-shadow: 0 6px 18px rgba(0,0,0,0.35);
    overflow: hidden;
  }
  .gold-band {
    position: absolute; left: 0; width: 100%; height: 21px;
    background: linear-gradient(90deg, var(--gold-light) 0%, var(--gold-mid) 35%, var(--gold-pale) 70%, var(--gold-mid) 100%);
  }
  .gold-band--top { top: 0; }
  .gold-band--bottom { bottom: 0; }

  .botanical-art {
    position: absolute; left: 0; top: 170px; width: 420px; height: 650px;
    background: radial-gradient(ellipse 60% 55% at 55% 45%, var(--botanical) 0%, rgba(251,239,210,0.55) 55%, rgba(255,255,255,0) 100%);
  }

  .product-title { font-weight: normal; }
  .title-pure, .title-oil {
    position: absolute;
    font-family: "Raleway", sans-serif; font-weight: 300;
    font-size: 46px; line-height: 1; color: var(--ink);
    letter-spacing: 1px;
  }
  .title-pure { left: 87px; top: 368px; }
  .title-oil { left: 310px; top: 506px; letter-spacing: 3px; }

  .title-jojoba {
    position: absolute; left: 20px; top: 402px;
    font-family: "Playfair Display", serif; font-weight: 500;
    font-size: 99px; line-height: 1; letter-spacing: -4px;
    background: linear-gradient(90deg, var(--gold-mid) 0%, var(--gold-light) 45%, var(--gold-mid) 70%, var(--gold-pale) 100%);
    -webkit-background-clip: text; background-clip: text;
    color: transparent;
  }
  .title-rule {
    position: absolute; left: 23px; top: 533px; width: 268px; height: 5px;
    background: linear-gradient(90deg, var(--gold-mid), var(--gold-light), var(--gold-mid));
  }

  .brand-name {
    position: absolute; left: 0; width: 100%; top: 664px;
    text-align: center;
    font-family: "Cinzel", serif; font-weight: 400;
    font-size: 19px; line-height: 1.25; color: var(--ink);
    letter-spacing: 1px;
  }

  .ingredients {
    position: absolute; left: 0; width: 100%; top: 736px;
    text-align: center;
    font-family: "Montserrat", sans-serif; font-weight: 500;
    font-size: 12px; letter-spacing: 1px; color: var(--ink);
  }

  .volume {
    position: absolute; left: 0; width: 100%; top: 760px;
    text-align: center;
    font-family: "Montserrat", sans-serif; font-weight: 600;
    font-size: 19px; color: var(--gold-text);
  }
</style>
</head>
<body>
  <div class="label">
    <div class="gold-band gold-band--top"></div>
    <div class="botanical-art" role="img" aria-label="Faint line drawing of a jojoba branch with leaves and seed pods"></div>

    <h1 class="product-title">
      <span class="title-pure">PURE</span>
      <span class="title-jojoba">JOJOBA</span>
      <span class="title-oil">OIL</span>
    </h1>
    <div class="title-rule"></div>

    <p class="brand-name">MARROWIN BROOK<br>SALON</p>
    <p class="ingredients">Ingredients: pure jojoba oil</p>
    <p class="volume">4 fl.oz/118 ml</p>

    <div class="gold-band gold-band--bottom"></div>
  </div>
</body>
</html>
```